Business Card Design - Pediatric Dentist

We need a business card for a new dental office. We are a pediatric dentist in Austin Tx. I would like a design that use bright green and if possible light blue.

Target Market(s)

Marketed to young moms

Industry/Entity Type

Dental

Contact Information for Business Card

Marcus Pell DDS
Bramblewood Family Dentistry
428 E. Marlowe Road. Austin TX 78690
(512) 555 0183.

In the back i would like to state "we take most insurances, Tova & Vitacover" & a map

Colors
add136
cadf82
85cae6

```html
<!DOCTYPE html>
<html lang="en">
<head>
<meta charset="utf-8">
<title>Bramblewood Family Dentistry – Business Card</title>
<link rel="stylesheet" href="https://fonts.googleapis.com/css2?family=Tinos&family=Roboto+Condensed:wght@400;700&family=Open+Sans:wght@700&display=swap">
<style>
  :root {
    --backdrop: #2c2c2c;
    --green: #add136;
    --sky: #99ccfd;
    --white: #ffffff;
    --ink: #111111;
    --mark-green: #3aa335;
  }
  * { margin: 0; padding: 0; box-sizing: border-box; }
  html, body { width: 1200px; height: 1000px; overflow: hidden; background: var(--backdrop); }
  .canvas { position: relative; width: 1200px; height: 1000px; }

  .card {
    position: absolute;
    width: 714px;
    height: 458px;
    overflow: hidden;
    box-shadow: 3px 4px 8px rgba(0,0,0,0.6);
  }
  .card-back  { left: 43px;  top: 28px; }
  .card-front { left: 441px; top: 514px; }
  .card-shapes { position: absolute; inset: 0; }

  .brand { position: absolute; display: flex; align-items: center; gap: 16px; }
  .brand-dot { width: 100px; height: 100px; border-radius: 50%; background: var(--mark-green); flex: none; }
  .brand-name {
    font-family: "Tinos", "Times New Roman", serif;
    font-size: 34px;
    line-height: 42px;
    color: var(--ink);
    white-space: nowrap;
  }
  .card-back .brand  { left: 362px; top: 256px; }
  .card-front .brand { left: 372px; top: 276px; }

  .tagline {
    position: absolute;
    left: 366px; top: 408px;
    font-family: "Open Sans", Arial, sans-serif;
    font-weight: 700;
    font-size: 14.5px;
    color: var(--ink);
  }

  .holder {
    position: absolute;
    right: 55px; top: 66px;
    text-align: right;
    font-family: "Roboto Condensed", "Arial Narrow", sans-serif;
  }
  .holder-name { font-weight: 700; font-size: 33px; line-height: 38px; color: var(--sky); }
  .holder-title { font-size: 21px; line-height: 24px; color: var(--green); }

  .contact {
    position: absolute;
    right: 394px; top: 328px;
    text-align: right;
    font-family: "Roboto Condensed", "Arial Narrow", sans-serif;
    font-style: normal;
    font-size: 20px;
    line-height: 28px;
    color: var(--green);
    white-space: nowrap;
  }
  .contact-practice { font-weight: 700; color: var(--sky); }
</style>
</head>
<body>
<main class="canvas">

  <section class="card card-back">
    <svg class="card-shapes" width="714" height="458" viewBox="0 0 714 458" aria-hidden="true">
      <rect width="714" height="458" fill="var(--green)"/>
      <circle cx="-67" cy="468" r="424" fill="var(--sky)"/>
      <circle cx="649" cy="-128" r="370" fill="var(--sky)"/>
    </svg>
    <div class="brand">
      <span class="brand-dot"></span>
      <p class="brand-name">Bramblewood<br>Family<br>Dentistry</p>
    </div>
    <p class="tagline">We Take Most Insurances, Tova &amp; Vitacover</p>
  </section>

  <section class="card card-front">
    <svg class="card-shapes" width="714" height="458" viewBox="0 0 714 458" aria-hidden="true">
      <rect width="714" height="458" fill="var(--green)"/>
      <circle cx="-67" cy="468" r="424" fill="var(--white)"/>
      <circle cx="649" cy="-128" r="370" fill="var(--white)"/>
    </svg>
    <div class="holder">
      <p class="holder-name">MARCUS PELL</p>
      <p class="holder-title">Doctor of Dental Surgery</p>
    </div>
    <address class="contact">
      <p class="contact-practice">Bramblewood Family Dentistry</p>
      <p>428 E. Marlowe Road. Austin TX 78690</p>
      <p>Telephone: (512) 555 0183</p>
    </address>
    <div class="brand">
      <span class="brand-dot"></span>
      <p class="brand-name">Bramblewood<br>Family<br>Dentistry</p>
    </div>
  </section>

</main>
</body>
</html>
```